Business Cards for Harborline Estates Partners, Inc.
Business Cards, Stationary, Etc.
Professional
Rocco Tamberlini
Broker
4710 SE Marigold Commons Lane
Suite 100
Boca Raton, Fl 33867
rocco@harborlinepfl.com
We prefer the use of icons, as opposed to wording for phone, fax, email.
I will need 2 options for each submission. The second option should allow for a picture to be inserted on the business card.
*Upon completion the winning designer will need to send a 2nd set of files, for another agent in the office. - Name, title, contact info to follow upon conclusion of Contest.

```html
<!DOCTYPE html>
<html lang="en">
<head>
<meta charset="utf-8">
<title>Harborline Estates Partners, Inc. — Stationery</title>
<link href="https://fonts.googleapis.com/css2?family=Montserrat:wght@400;600;700&display=swap" rel="stylesheet">
<style>
  :root{
    --backdrop:#2e2e30;
    --paper:#ffffff;
    --paper-shade:#f2f2f2;
    --navy:#2c3b5e;
    --sage:#6f8270;
    --ink:#3a3a3a;
    --muted:#8a8a8a;
    --ghost:#ececec;
    --label:#9a9a9a;
  }
  *{box-sizing:border-box;margin:0;padding:0}
  html,body{width:1200px;height:312px;overflow:hidden;background:var(--backdrop);font-family:"Montserrat",sans-serif}
  .canvas{position:relative;width:1200px;height:312px}
  .sheet{position:absolute;background:var(--paper);box-shadow:0 2px 6px rgba(0,0,0,.45)}
  .brand{display:flex;align-items:center;gap:3px;color:var(--navy);font-weight:700;letter-spacing:.3px}
  .brand-mark{display:inline-block;background:var(--navy)}
  .label{position:absolute;color:var(--label);font-size:5px;text-transform:uppercase;letter-spacing:.4px;text-align:center}
  .ghost{position:absolute;background:var(--ghost)}

  /* business cards */
  .card{width:88px;height:50px}
  .card .brand{position:absolute;font-size:5px}
  .card .brand-mark{width:5px;height:5px}
  .card-front .brand{top:7px;left:7px}
  .card-details{position:absolute;left:7px;bottom:6px;font-size:3.4px;line-height:1.35;color:var(--ink)}
  .card-details strong{font-size:4.4px;color:var(--navy)}
  .card-back .brand{top:50%;left:50%;transform:translate(-50%,-50%);font-size:6px}
  .card-back .brand-mark{width:6px;height:6px}
  .card-photo{position:absolute;right:6px;top:8px;width:20px;height:26px;background:linear-gradient(#d9d9d9,#c4c4c4)}

  /* letterhead */
  .letterhead{width:204px;height:264px;top:16px}
  .letterhead .brand{position:absolute;top:10px;left:50%;transform:translateX(-50%);font-size:7px}
  .letterhead .brand-mark{width:7px;height:7px}
  .letterhead .ghost{right:14px;bottom:24px;width:64px;height:64px}
  .letterhead-footer{position:absolute;left:14px;bottom:12px;font-size:3.6px;line-height:1.4;color:var(--muted)}
  .letterhead-footer .rule{display:block;width:2px;height:14px;background:var(--navy);position:absolute;left:-5px;top:0}
  .letterhead-two .ghost{left:50%;top:50%;transform:translate(-50%,-50%);width:78px;height:78px;right:auto;bottom:auto}

  /* #10 envelopes */
  .envelope{width:228px;height:100px}
  .envelope .brand{position:absolute;top:8px;left:9px;font-size:5.5px}
  .envelope .brand-mark{width:5.5px;height:5.5px}
  .return-address{position:absolute;top:17px;left:9px;font-size:3.2px;line-height:1.4;color:var(--muted)}
  .envelope .ghost{left:40px;top:28px;width:52px;height:52px}

  /* flap stack */
  .flap-stack{position:absolute;left:910px;top:14px}
</style>
</head>
<body>
<main class="canvas">

  <!-- business cards -->
  <section class="cards">
    <div class="sheet card card-front" style="left:22px;top:110px">
      <div class="brand"><span class="brand-mark"></span>HARBORLINE</div>
      <div class="card-details">
        <strong>Rocco Tamberlini</strong><br>Broker<br>
        ☏ 561.555.0142<br>✉ rocco@harborlinepfl.com<br>
        4710 SE Marigold Commons Lane, Suite 100
      </div>
    </div>
    <div class="sheet card card-back" style="left:118px;top:110px">
      <div class="brand"><span class="brand-mark"></span>HARBORLINE</div>
    </div>
    <div class="label" style="left:22px;top:162px;width:88px">Option One Front</div>
    <div class="label" style="left:118px;top:162px;width:88px">Option One Back</div>

    <div class="sheet card card-front" style="left:22px;top:178px">
      <div class="brand"><span class="brand-mark"></span>HARBORLINE</div>
      <div class="card-photo" role="img" aria-label="Space for agent portrait photo"></div>
      <div class="card-details">
        <strong>Rocco Tamberlini</strong><br>Broker<br>
        ☏ 561.555.0142<br>✉ rocco@harborlinepfl.com
      </div>
    </div>
    <div class="sheet card card-back" style="left:118px;top:178px">
      <div class="brand"><span class="brand-mark"></span>HARBORLINE</div>
    </div>
    <div class="label" style="left:22px;top:230px;width:88px">Option Two Front</div>
    <div class="label" style="left:118px;top:230px;width:88px">Option Two Back</div>
  </section>

  <!-- letterheads -->
  <section class="letterheads">
    <div class="sheet letterhead" style="left:222px">
      <div class="brand"><span class="brand-mark"></span>HARBORLINE</div>
      <div class="ghost" role="img" aria-label="Faint brand watermark"></div>
      <div class="letterhead-footer">
        <span class="rule"></span>
        Harborline Estates Partners, Inc.<br>
        4710 SE Marigold Commons Lane, Suite 100<br>
        Boca Raton, Fl 33867
      </div>
    </div>
    <div class="label" style="left:222px;top:286px;width:204px">Letterhead Page One</div>

    <div class="sheet letterhead letterhead-two" style="left:436px">
      <div class="brand"><span class="brand-mark"></span>HARBORLINE</div>
      <div class="ghost" role="img" aria-label="Faint brand watermark"></div>
    </div>
    <div class="label" style="left:436px;top:286px;width:204px">Letterhead Page Two</div>
  </section>

  <!-- envelopes -->
  <section class="envelopes">
    <div class="sheet envelope" style="left:664px;top:36px">
      <div class="brand"><span class="brand-mark"></span>HARBORLINE</div>
      <div class="return-address">
        4710 SE Marigold Commons Lane, Suite 100<br>Boca Raton, Fl 33867
      </div>
      <div class="ghost" role="img" aria-label="Faint brand watermark"></div>
    </div>
    <div class="label" style="left:664px;top:142px;width:228px">Envelope Front</div>

    <div class="sheet envelope" style="left:664px;top:164px">
      <div class="brand"><span class="brand-mark"></span>HARBORLINE</div>
      <div class="return-address">
        4710 SE Marigold Commons Lane, Suite 100<br>Boca Raton, Fl 33867
      </div>
      <div class="ghost" role="img" aria-label="Faint brand watermark"></div>
    </div>
    <div class="label" style="left:664px;top:270px;width:228px">Envelope Back</div>

    <svg class="flap-stack" width="270" height="270" viewBox="0 0 270 270">
      <g>
        <rect x="0" y="0" width="266" height="110" fill="var(--paper)"/>
        <path d="M0 0 H266 V28 L150 62 H116 L0 28 Z" fill="var(--navy)"/>
        <rect x="90" y="8" width="6" height="6" fill="var(--paper)"/>
        <text x="100" y="14" font-family="Montserrat, sans-serif" font-size="6" font-weight="700" fill="var(--paper)">HARBORLINE</text>
      </g>
      <g transform="translate(0,70)">
        <rect x="0" y="0" width="266" height="110" fill="var(--paper)"/>
        <path d="M0 0 H266 V28 L150 62 H116 L0 28 Z" fill="var(--sage)"/>
        <text x="133" y="14" text-anchor="middle" font-family="Montserrat, sans-serif" font-size="6" font-weight="700" fill="var(--paper)">HARBORLINE</text>
      </g>
      <g transform="translate(0,140)">
        <rect x="0" y="0" width="266" height="110" fill="var(--paper)" stroke="#dcdcdc"/>
        <path d="M0 0 H266 V28 L150 62 H116 L0 28 Z" fill="var(--paper-shade)" stroke="#d6d6d6"/>
        <text x="133" y="14" text-anchor="middle" font-family="Montserrat, sans-serif" font-size="6" font-weight="700" fill="var(--navy)">HARBORLINE</text>
      </g>
      <text x="133" y="262" text-anchor="middle" font-family="Montserrat, sans-serif" font-size="5" fill="var(--label)" letter-spacing=".4">ENVELOPE FLAP COLORS</text>
    </svg>
  </section>

</main>
</body>
</html>
```